Business Card Design/Stationary Design

We would like designers to submit cool, hip business card designs (plus stationary designs) for a new, upstart software development company located in Toronto.
If you have any questions, please email us.
For inspiration on designs:
http://cardmuse.example/cool-business-cards/
http://layoutnotes.example/2008/05/36-cool-business-cards-you-should%E2%80%99ve-seen.html
http://gigharbor.example/general/18-smokin-hot-business-card-designs/

Card info:

Selvakumar (Selv) Nadarasan

Founder and CEO

47 Brindle Court, Suite 311

Toronto, ON M4K 2T8

Phone: 647-512-7730

Mobile: 416-273-5094

Fax: 647-512-7731

Email: selvakumar.nadarasan@mailbrook.example

www.quendrix.example
Updates

Hi everyone,

In terms of all the designs I have seen so far, here is what I like:

1.  I really like the "back" part of this design.  The "front" looks pretty decent as well, but for the "front", look at #2 on this list.  I like that.

http://www.pitchboard.example/image.aspx?imageLocation=1000_10001_2000_image.jpg&type=design300px&whiteLabelCustId=9999

2. "Side 1" of this I like, the front needs to be reworked.

http://www.pitchboard.example/image.aspx?imageLocation=1000_10002_2000_image.png&type=design300px&whiteLabelCustId=9999

3. http://www.pitchboard.example/image.aspx?imageLocation=1000_10003_2000_image.jpg&type=design300px&whiteLabelCustId=9999

4. http://www.pitchboard.example/image.aspx?imageLocation=1000_10004_2000_image.jpg&type=design300px&whiteLabelCustId=9999

Target Market(s)

We are focused on enterprise customers right now, so businesses with a long-term goal of also reaching out to the consumer market as well.

Industry/Entity Type

Software

Requirements
Must have
• Must look cool, ultra-modern, clean and eye-catching. Must incorporate our logo and the colors found in the logo.

```html
<!DOCTYPE html>
<html lang="en">
<head>
<meta charset="utf-8">
<title>Quendrix Business Card</title>
<link href="https://fonts.googleapis.com/css2?family=Alegreya+Sans:ital,wght@0,500;1,400&display=swap" rel="stylesheet">
<style>
  :root {
    --paper: #ffffff;
    --ink: #1a1a1a;
    --olive: #93a81e;
    --teal: #17a98a;
    --tab: #0ea575;
    --mark: #8dbb2a;
  }
  html, body {
    margin: 0;
    padding: 0;
    width: 1200px;
    height: 2165px;
    overflow: hidden;
    background: var(--paper);
  }
  .card {
    position: relative;
    width: 1200px;
    height: 2165px;
    background: var(--paper);
    font-family: "Alegreya Sans", "Trebuchet MS", sans-serif;
    color: var(--ink);
  }
  .brand-tab {
    position: absolute;
    left: 1120px;
    top: 388px;
    width: 80px;
    height: 210px;
    background: var(--tab);
    border-radius: 40px 0 0 40px;
  }
  .brand {
    position: absolute;
    left: 330px;
    top: 380px;
    display: flex;
    align-items: center;
    gap: 46px;
  }
  .brand-dot {
    width: 210px;
    height: 210px;
    border-radius: 50%;
    background: var(--mark);
  }
  .brand-name {
    font-style: normal;
    font-weight: 500;
    font-size: 122px;
    line-height: 1;
    color: var(--ink);
  }
  .details {
    position: absolute;
    right: 87px;
    top: 1140px;
    text-align: right;
    font-style: italic;
    font-weight: 400;
    letter-spacing: 3px;
  }
  .details p { margin: 0; }
  .person-name {
    font-size: 58px;
    line-height: 70px;
    color: var(--olive);
  }
  .person-title {
    font-size: 45px;
    line-height: 56px;
  }
  .address {
    margin-top: 80px !important;
    font-size: 44px;
    line-height: 67px;
  }
  .contact {
    margin-top: 90px !important;
    font-size: 44px;
    line-height: 67px;
  }
  .contact .label { color: var(--teal); }
  .contact .email { letter-spacing: 1px; font-size: 42px; }
  .contact .web { color: var(--teal); }
</style>
</head>
<body>
  <main class="card">
    <div class="brand-tab"></div>
    <div class="brand">
      <span class="brand-dot"></span>
      <span class="brand-name">Quendrix</span>
    </div>
    <section class="details">
      <p class="person-name">Selvakumar (Selv) Nadarasan</p>
      <p class="person-title">Founder and CEO</p>
      <p class="address">47 Brindle Court, Suite 311<br>Toronto, ON M4K 2T8</p>
      <p class="contact">
        <span class="label">Phone:</span> 647-512-7730<br>
        <span class="label">Mobile:</span> 416-273-5094<br>
        <span class="label">Fax:</span> 647-512-7731<br>
        <span class="email"><span class="label">Email:</span> selvakumar.nadarasan@mailbrook.example</span><br>
        <span class="web">www.quendrix.example</span>
      </p>
    </section>
  </main>
</body>
</html>
```